OPV Brantmoor Freight Limited

We need the buissnes card to be very exclusive. As we are all young in our company. We need this to be the gate to make our clients feel deep interest for us.

We are focused in as International Trade advisors, and our products go from Oil Tanker Ships to Rubber balls for dogs.

Our Slogan is Trading Near and Far.
And our main marketing will be through Internet.

We were stablished in 2009 In Mexico and we also have offices in Hong Kong.
We have representatives in China and Europe.

Target Market(s)

Is every company or Individual that wants to develop an International Project or product development or Logistic service of Goods and people.
Some of our current projects are Ship Brokerage, Mine Brokerage, Real State and Product Pormotional development.

Industry/Entity Type

It Company

Requirements
Must have
• Our Logo and slogan, and make the card accoriding to the logo.
Nice to have
• Our Colors

```html
<!DOCTYPE html>
<html lang="en">
<head>
<meta charset="utf-8">
<title>OPV Brantmoor Freight Limited – Business Card</title>
<link rel="stylesheet" href="https://fonts.googleapis.com/css2?family=Michroma&family=Orbitron:wght@700&family=Jura:wght@400;500&display=swap">
<style>
  :root {
    --page-bg: #e6e7e9;
    --blue-deep: #2c3f8f;
    --blue-mid: #34519f;
    --blue-light: #3f6db4;
    --sky: #4fb3e8;
    --lime: #8cc63f;
    --green-deep: #5f9e2a;
    --green-mid: #78b535;
    --green-light: #8bc540;
    --white: #ffffff;
  }
  * { box-sizing: border-box; margin: 0; padding: 0; }
  html, body { width: 1200px; height: 900px; overflow: hidden; }
  body {
    background: var(--page-bg);
    position: relative;
    font-family: "Jura", sans-serif;
  }
  .card {
    position: absolute;
    width: 640px;
    height: 366px;
    overflow: hidden;
    box-shadow: 0 6px 18px rgba(0,0,0,0.25);
  }
  .card--front {
    left: 70px; top: 110px;
    background: linear-gradient(135deg, var(--blue-deep) 0%, var(--blue-mid) 55%, var(--blue-light) 100%);
  }
  .card--back {
    left: 490px; top: 430px;
    background: radial-gradient(ellipse at 55% 45%, var(--green-light) 0%, var(--green-mid) 55%, var(--green-deep) 100%);
  }
  .map-backdrop { position: absolute; inset: 0; }
  .card--front .map-backdrop {
    background: radial-gradient(ellipse at 75% 30%, rgba(80,130,200,0.35) 0%, rgba(80,130,200,0) 60%),
                radial-gradient(ellipse at 20% 60%, rgba(80,130,200,0.25) 0%, rgba(80,130,200,0) 55%);
  }
  .card--back .map-backdrop {
    background: radial-gradient(ellipse at 80% 70%, rgba(150,205,80,0.45) 0%, rgba(150,205,80,0) 55%),
                radial-gradient(ellipse at 15% 75%, rgba(95,160,40,0.4) 0%, rgba(95,160,40,0) 50%);
  }
  .brand {
    position: absolute;
    display: flex;
    flex-direction: column;
    align-items: center;
  }
  .card--front .brand { left: 170px; top: 60px; width: 300px; }
  .card--back .brand { left: 50px; top: 50px; width: 250px; }
  .brand__mark { border-radius: 50%; }
  .card--front .brand__mark { width: 170px; height: 170px; background: var(--lime); }
  .card--back .brand__mark { width: 150px; height: 150px; background: var(--white); }
  .brand__name {
    font-family: "Michroma", sans-serif;
    line-height: 1;
    margin-top: 14px;
  }
  .card--front .brand__name { font-size: 54px; color: var(--lime); }
  .card--back .brand__name { font-size: 44px; color: var(--white); }
  .brand__slogan {
    font-family: "Jura", sans-serif;
    font-weight: 500;
    margin-top: 6px;
    white-space: nowrap;
  }
  .card--front .brand__slogan { font-size: 15px; color: var(--sky); }
  .card--back .brand__slogan { font-size: 13px; color: var(--white); }
  .contact {
    position: absolute;
    right: 60px; top: 62px;
    text-align: right;
    color: var(--white);
  }
  .contact__name {
    font-family: "Orbitron", sans-serif;
    font-weight: 700;
    font-size: 23px;
    letter-spacing: 0.5px;
  }
  .contact__title {
    font-family: "Orbitron", sans-serif;
    font-weight: 700;
    font-size: 14px;
    margin-top: 4px;
    margin-bottom: 8px;
  }
  .contact__line {
    font-size: 20px;
    font-weight: 500;
    letter-spacing: 1px;
    line-height: 1.25;
  }
</style>
</head>
<body>
  <section class="card card--front" aria-label="Card front">
    <div class="map-backdrop" role="img" aria-label="Faint world map backdrop in deep blue"></div>
    <div class="brand">
      <span class="brand__mark" aria-hidden="true"></span>
      <span class="brand__name">OPV</span>
      <span class="brand__slogan">Trading Near and Far</span>
    </div>
  </section>

  <section class="card card--back" aria-label="Card back">
    <div class="map-backdrop" role="img" aria-label="Faint world map backdrop in green"></div>
    <div class="brand">
      <span class="brand__mark" aria-hidden="true"></span>
      <span class="brand__name">OPV</span>
      <span class="brand__slogan">Trading Near and Far</span>
    </div>
    <div class="contact">
      <p class="contact__name">First Last</p>
      <p class="contact__title">Title</p>
      <p class="contact__line">888.888.8888</p>
      <p class="contact__line">first.last@opv.com</p>
      <p class="contact__line">1234 Street</p>
      <p class="contact__line">Town, AK 55501</p>
    </div>
  </section>
</body>
</html>
```